Strength and Conditioning Business needs a logo design

We need a logo design for a fitness company based in South Carolina called "K7R Motion Dynamics". We are a group of Strength and Conditioning Coaches that work with youth, high school, collegiate, and professional athletes. We also train general population clients that are looking to improve their overall fitness. Our primary mission is to make sure our athletes are able to gain the greatest benefits from training that will allow them to excel in their sport. We use heavy chains, kettle bells, resistance bands, dumbbells, prowlers (sleds), and multi-functional machines for training. We have a dynamic and collaborative approach that utilizes high-intensity intervals combined with speed, power, agility, and strength training.

Industry/Entity Type

Fitness

Contact Information for Business Card

K7R Motion Dynamics
Lorenzo Baptiste, MS, CSCS, FMSC
Director of Sports Performance
Columbia, SC
Phone: (555) 318-7046
Email: k7rmotiondynamics@quikmailbox.net
Instagram: lift_mentor_lb

Font styles to use
Sans Serif

Colors
9bcb3c
ffffff
000000
474747
ec1f27
7f7f7f
0456a4

Requirements
Must have
• I would like to have a black card with either lime green or bold blue accents along with white and silver. On the back, I would like the name 'K7R Motion Dynamics' with a subheading that says, 'Strength and Conditioning.'
Nice to have
• I really like the designs of the cards I uploaded. For the logo, something clean, bold, and eye-catching would be great.
Should not have
• I do not want a logo that will make it difficult to read.

```html
<!DOCTYPE html>
<html lang="en">
<head>
<meta charset="utf-8">
<title>K7R Motion Dynamics – Business Card</title>
<link rel="stylesheet" href="https://fonts.googleapis.com/css2?family=Open+Sans:wght@400;600;700&display=swap">
<style>
  :root {
    --backdrop: #2a2624;
    --card-black: #0d0d0d;
    --card-back: #1c1c1c;
    --accent-lime: #9bcb3c;
    --accent-lime-deep: #86b52f;
    --text-white: #ffffff;
    --text-grey: #cfcfcf;
    --text-mid: #7f7f7f;
    --divider: #474747;
    --silver: #c4c4c4;
    --band-text: #0d0d0d;
  }
  html, body {
    margin: 0;
    padding: 0;
    width: 1200px;
    height: 716px;
    overflow: hidden;
    background: var(--backdrop);
  }
  .canvas {
    position: relative;
    width: 1200px;
    height: 716px;
  }
  .card {
    position: absolute;
    top: 209px;
    width: 520px;
    height: 298px;
    box-shadow: 0 10px 30px rgba(0,0,0,0.5);
    overflow: hidden;
  }
  .card-front { left: 50px; background: var(--card-black); }
  .card-back  { left: 630px; background: var(--card-back); }

  .front-band {
    position: absolute;
    left: 0; top: 0;
    width: 520px; height: 298px;
  }
  .band-address {
    font-family: "Open Sans", sans-serif;
    font-weight: 700;
    font-size: 12px;
    fill: var(--band-text);
    letter-spacing: 0.5px;
  }

  .brand-lockup {
    position: absolute;
    left: 30px;
    top: 58px;
    width: 200px;
    display: flex;
    align-items: center;
    gap: 10px;
  }
  .brand-dot {
    width: 26px; height: 26px;
    border-radius: 50%;
    background: var(--accent-lime);
    flex: none;
  }
  .brand-name {
    font-family: "Open Sans", sans-serif;
    font-weight: 700;
    font-size: 17px;
    line-height: 1.15;
    color: var(--text-white);
    text-transform: uppercase;
  }

  .divider {
    position: absolute;
    left: 242px;
    top: 38px;
    width: 1px;
    height: 118px;
    background: var(--divider);
  }

  .contact {
    position: absolute;
    left: 258px;
    top: 38px;
    font-family: "Open Sans", sans-serif;
    color: var(--text-grey);
  }
  .contact-name {
    margin: 0;
    font-weight: 700;
    font-size: 15px;
    color: var(--accent-lime);
    text-transform: uppercase;
    letter-spacing: 0.3px;
  }
  .contact-credentials {
    margin: 2px 0 0;
    font-size: 11.5px;
  }
  .contact-title {
    margin: 1px 0 8px;
    font-size: 10.5px;
  }
  .contact-list {
    list-style: none;
    margin: 0;
    padding: 0;
    font-size: 10.5px;
  }
  .contact-list li {
    display: flex;
    align-items: center;
    gap: 6px;
    margin-bottom: 3px;
  }
  .contact-icon {
    width: 11px; height: 11px;
    flex: none;
  }

  .back-lockup {
    position: absolute;
    left: 0; right: 0;
    top: 108px;
    display: flex;
    flex-direction: column;
    align-items: center;
    gap: 8px;
  }
  .back-mark {
    display: flex;
    align-items: center;
    gap: 14px;
  }
  .back-dot {
    width: 34px; height: 34px;
    border-radius: 50%;
    background: var(--silver);
  }
  .back-name {
    font-family: "Open Sans", sans-serif;
    font-weight: 700;
    font-size: 28px;
    color: var(--silver);
    text-transform: uppercase;
    letter-spacing: 1px;
  }
  .back-subheading {
    margin: 0;
    font-family: "Open Sans", sans-serif;
    font-weight: 600;
    font-size: 13px;
    color: var(--accent-lime);
    text-transform: uppercase;
    letter-spacing: 3px;
  }
</style>
</head>
<body>
<main class="canvas">

  <section class="card card-front" aria-label="Business card front">
    <svg class="front-band" viewBox="0 0 520 298">
      <path d="M0 170 Q300 200 520 298 L0 298 Z" fill="var(--accent-lime)"/>
      <path d="M0 180 Q300 212 500 298 L0 298 Z" fill="var(--accent-lime-deep)" opacity="0.85"/>
      <path id="addressPath" d="M90 202 Q270 222 450 290" fill="none"/>
      <text class="band-address">
        <textPath href="#addressPath">4820 PLACEHOLDER AVE, COLUMBIA, SC</textPath>
      </text>
    </svg>

    <div class="brand-lockup">
      <span class="brand-dot"></span>
      <span class="brand-name">K7R Motion Dynamics</span>
    </div>

    <div class="divider"></div>

    <div class="contact">
      <p class="contact-name">Lorenzo Baptiste</p>
      <p class="contact-credentials">MS, CSCS, FMSC</p>
      <p class="contact-title">Director of Sports Performance</p>
      <ul class="contact-list">
        <li>
          <svg class="contact-icon" viewBox="0 0 12 12" aria-label="Phone">
            <rect width="12" height="12" rx="2" fill="var(--accent-lime)"/>
            <path d="M3.5 2.5 L5 4 L4.2 5 Q5 6.8 7 7.8 L8 7 L9.5 8.5 L8.5 9.6 Q4.5 9 2.4 3.5 Z" fill="var(--card-black)"/>
          </svg>
          (555) 318-7046
        </li>
        <li>
          <svg class="contact-icon" viewBox="0 0 12 12" aria-label="Email">
            <rect width="12" height="12" rx="2" fill="var(--accent-lime)"/>
            <rect x="2.5" y="3.5" width="7" height="5" fill="none" stroke="var(--card-black)" stroke-width="0.9"/>
            <path d="M2.5 3.5 L6 6.4 L9.5 3.5" fill="none" stroke="var(--card-black)" stroke-width="0.9"/>
          </svg>
          k7rmotiondynamics@quikmailbox.net
        </li>
        <li>
          <svg class="contact-icon" viewBox="0 0 12 12" aria-label="Social handle">
            <rect width="12" height="12" rx="2" fill="var(--accent-lime)"/>
          </svg>
          lift_mentor_lb
        </li>
      </ul>
    </div>
  </section>

  <section class="card card-back" aria-label="Business card back">
    <div class="back-lockup">
      <div class="back-mark">
        <span class="back-dot"></span>
        <span class="back-name">K7R Motion Dynamics</span>
      </div>
      <p class="back-subheading">Strength and Conditioning</p>
    </div>
  </section>

</main>
</body>
</html>
```